Property inspection company needs logo/business card design

A new, home, commercial, and multi dwelling inspection company needs help with a new logo and hence business cards.

Time is extended for the rest of the week.

Font styles to use
Sans Serif

Colors
ec1f27
0255a3
ffffff

```html
<!DOCTYPE html>
<html lang="en">
<head>
<meta charset="utf-8">
<title>Dan Harlowe Property Inspections – Business Card</title>
<link href="https://fonts.googleapis.com/css2?family=Montserrat:wght@500;700&family=Roboto:wght@400;500&display=swap" rel="stylesheet">
<style>
  :root {
    --red: #ec1f27;
    --blue: #2e3192;
    --brand-blue: #0255a3;
    --purple: #7a2a7a;
    --white: #ffffff;
    --paper: #fafafa;
    --stage: #1f1f1f;
    --faint: #e6e6e6;
  }
  * { box-sizing: border-box; margin: 0; padding: 0; }
  html, body {
    width: 1200px; height: 1200px; overflow: hidden;
    background: var(--stage);
  }
  .canvas { position: relative; width: 1200px; height: 1200px; }
  .card {
    position: absolute; left: 127px; width: 945px; height: 540px;
    background: var(--paper); border-radius: 26px; overflow: hidden;
    font-family: "Roboto", sans-serif;
  }
  .card--back { top: 40px; }
  .card--front { top: 620px; }

  /* Back */
  .back-mark {
    position: absolute; left: 230px; top: 205px;
    display: flex; align-items: center; gap: 22px;
  }
  .back-mark__circle {
    width: 110px; height: 110px; border-radius: 50%;
    border: 9px solid var(--red);
  }
  .wordmark {
    font-family: "Montserrat", sans-serif; font-weight: 700;
    color: var(--blue); line-height: 1;
  }
  .wordmark__name { font-size: 46px; letter-spacing: 1px; }
  .wordmark__sub { font-size: 17px; letter-spacing: 3.2px; margin-top: 10px; }
  .back-faint {
    position: absolute; right: -200px; top: 130px;
    width: 380px; height: 380px; border-radius: 50%;
    background: var(--faint); opacity: .7;
  }

  /* Front */
  .front-mark { position: absolute; left: 130px; top: 60px; }
  .front-mark .wordmark__name { font-size: 52px; }
  .front-mark .wordmark__sub { font-size: 19px; letter-spacing: 3.6px; }
  .person { position: absolute; left: 95px; top: 210px; }
  .person__name {
    font-family: "Montserrat", sans-serif; font-weight: 500;
    font-size: 34px; color: var(--blue);
  }
  .person__title {
    font-family: "Montserrat", sans-serif; font-weight: 500;
    font-size: 24px; color: var(--red); margin-top: 2px;
  }
  .contacts { list-style: none; margin-top: 18px; }
  .contacts li {
    display: flex; align-items: center; gap: 12px;
    font-size: 21px; color: var(--blue); line-height: 31px;
  }
  .contacts svg { width: 20px; height: 20px; fill: var(--red); flex: none; }
  .front-circle {
    position: absolute; left: 625px; top: 80px;
    width: 255px; height: 255px; border-radius: 50%;
    border: 13px solid var(--red);
  }
  .address {
    position: absolute; right: 60px; top: 355px; text-align: right;
    font-size: 22px; line-height: 30px; color: var(--blue); font-style: normal;
  }
  .tagline-band {
    position: absolute; left: 0; bottom: 0; width: 100%; height: 62px;
    background: linear-gradient(90deg, var(--red) 0%, var(--red) 15%, var(--purple) 62%, var(--blue) 100%);
    color: var(--white); font-size: 22px; letter-spacing: .3px;
    display: flex; align-items: center; padding-left: 95px;
  }
</style>
</head>
<body>
<main class="canvas">

  <section class="card card--back" aria-label="Card back">
    <div class="back-faint" aria-hidden="true"></div>
    <div class="back-mark">
      <div class="back-mark__circle" aria-hidden="true"></div>
      <div class="wordmark">
        <div class="wordmark__name">DAN HARLOWE</div>
        <div class="wordmark__sub">PROPERTY INSPECTIONS INC</div>
      </div>
    </div>
  </section>

  <section class="card card--front" aria-label="Card front">
    <div class="front-mark wordmark">
      <div class="wordmark__name">DAN HARLOWE</div>
      <div class="wordmark__sub">PROPERTY INSPECTIONS INC</div>
    </div>

    <div class="person">
      <h1 class="person__name">Dan Harlowe</h1>
      <p class="person__title">CEO/Founder</p>
      <ul class="contacts">
        <li>
          <svg viewBox="0 0 20 20" aria-hidden="true"><rect x="4" y="1" width="12" height="18" rx="2"/><rect x="6" y="3" width="8" height="7" fill="#fafafa"/></svg>
          555-201-4830
        </li>
        <li>
          <svg viewBox="0 0 20 20" aria-hidden="true"><path d="M4 2l4 0 1 5-2 1.5c1 2.5 3 4.5 5.5 5.5L14 12l5 1v4c0 1-1 2-2 2C9 19 1 11 1 4c0-1 1-2 3-2z"/></svg>
          555-318-7742
        </li>
        <li>
          <svg viewBox="0 0 20 20" aria-hidden="true"><path d="M1 4h18v12H1z"/><path d="M1 4l9 7 9-7" fill="none" stroke="#fafafa" stroke-width="1.6"/></svg>
          dan@harloweinspect.com
        </li>
      </ul>
    </div>

    <div class="front-circle" aria-hidden="true"></div>

    <address class="address">
      118 Cedar Ridge Road<br>
      Suite 210, Lakeview<br>
      MI 49000
    </address>

    <div class="tagline-band">New home, commercial, and multi dwelling inspection</div>
  </section>

</main>
</body>
</html>
```